Spiritual Support flyer design

I offer a range of spiritual support options from a drop in group to meditation. I work alone in two locations, one at home and the other in the local town centre therapy centre. I do not want people to be confused about where to go for each item so thought one side could be the town centre group and the other side of the leaflet could be the things I offer from home. I need to find a way to present a list of things I do and make it look inviting so people want to contact me. I want it to feel inspirational, uplifting, light hearted, with a gentle feel of support or coming home to somewhere safe. The leaflet needs to look eye catching as it will be where there are many other leaflets the same size (A5). I love purples, as they tend to be spiritual colours or the look below of light bursting through the clouds seems appropriate picture wise. I do not have a logo.
The title can be Quiet Harbour. On one side I would like to introduce a Spiritual Experiences drop-in group held at the Larkfield Centre, Colchester 1-2pm every four weeks to share spiritual experiences with others. I can give you more words for that when you are ready. The other side needs to feature the things I offer from my own home which are: Spiritual Counselling, Private email guidance, Meditation one to one, and Quiet Harbour Days, which are like a days retreat. It might be a good idea to mention prices but not in an obvious way, so have that just readable in small print.

Town

```html
<!DOCTYPE html>
<html lang="en">
<head>
<meta charset="utf-8">
<title>Quiet Harbour – Spiritual Support Flyer</title>
<link rel="stylesheet" href="https://fonts.googleapis.com/css2?family=Nunito+Sans:wght@400;600;700;800&display=swap">
<style>
  :root {
    --backdrop: #000000;
    --paper: #ffffff;
    --plum: #6c1466;
    --orchid: #8f3f9d;
    --sky-row: #c4dcf3;
    --ink: #1f1f1f;
    --rose: #e6336f;
    --mist: #d9d9d9;
  }
  * { margin: 0; padding: 0; box-sizing: border-box; }
  html, body { width: 1200px; height: 870px; overflow: hidden; background: var(--backdrop); }
  body { font-family: "Nunito Sans", Arial, sans-serif; position: relative; }

  .flyer-side { position: absolute; top: 42px; height: 788px; overflow: hidden; }

  /* Front: drop-in group */
  .side-group { left: 34px; width: 556px; background: #2a1a2c; }
  .group-header {
    position: absolute; left: 0; top: 0; width: 100%; height: 125px;
    background: var(--orchid); color: var(--paper); text-align: center;
  }
  .group-title { font-size: 36px; font-weight: 800; letter-spacing: 0.5px; padding-top: 38px; line-height: 1; }
  .group-subtitle { font-size: 23px; font-weight: 600; margin-top: 4px; }
  .sky-photo {
    position: absolute; left: 0; top: 125px; width: 100%; height: 663px;
    background:
      radial-gradient(ellipse 60% 45% at 80% 70%, #ffffff 0%, #f0dff3 25%, rgba(200,160,210,0) 70%),
      linear-gradient(180deg, #c6c0c8 0%, #c9a6cf 30%, #b27fc0 60%, #8d5a9c 76%, #2b1a2e 82%, #1c111e 100%);
  }
  .group-copy {
    position: absolute; left: 52px; top: 146px; width: 452px;
    text-align: center; font-size: 13.6px; line-height: 17.6px; color: var(--ink);
  }
  .group-copy p + p { margin-top: 17.6px; }
  .group-venue {
    position: absolute; left: 0; bottom: 36px; width: 100%;
    text-align: center; color: var(--rose); font-size: 15px; line-height: 19px; font-weight: 600;
  }

  /* Back: home sessions */
  .side-home { left: 611px; width: 555px; background: var(--paper); }
  .home-title {
    position: absolute; top: 40px; width: 100%; text-align: center;
    color: var(--plum); font-size: 39px; font-weight: 700; letter-spacing: 0.5px; line-height: 1;
  }
  .home-address {
    position: absolute; top: 86px; width: 100%; text-align: center;
    color: var(--ink); font-size: 13.5px; font-weight: 600; line-height: 18px;
  }
  .price-list { position: absolute; left: 48px; top: 144px; width: 458px; }
  .service-name {
    background: var(--plum); color: var(--paper);
    font-size: 14px; font-weight: 700; padding: 0 12px; height: 26px; line-height: 26px;
  }
  .service-row {
    background: var(--sky-row); display: flex; align-items: center; justify-content: space-between;
    padding: 0 38px 0 12px; font-size: 13.5px; line-height: 17.5px; color: var(--ink);
  }
  .service-price { color: var(--plum); font-size: 22px; font-weight: 700; }
  .row-tall { height: 50px; }
  .row-short { height: 30px; }
  .row-mid { height: 48px; }
  .row-day { height: 33px; }

  .meditation-figure {
    position: absolute; left: 160px; top: 418px; width: 235px; height: 200px;
    border-radius: 40px;
    background: radial-gradient(ellipse at 50% 55%, #e4e4e4 0%, #f2f2f2 55%, #ffffff 100%);
  }

  .contact-band {
    position: absolute; left: 0; top: 636px; width: 100%; height: 152px;
    background: var(--plum); color: var(--paper);
  }
  .contact-line { position: absolute; left: 92px; display: flex; align-items: baseline; }
  .contact-label { width: 143px; font-size: 11px; font-weight: 600; }
  .contact-sep { width: 48px; font-size: 11px; }
  .contact-value { font-size: 15px; font-weight: 600; }
</style>
</head>
<body>

<section class="flyer-side side-group">
  <div class="sky-photo" role="img" aria-label="Silhouette of a person raising their arms towards light bursting through purple evening clouds above a dark treeline"></div>
  <header class="group-header">
    <h1 class="group-title">SPIRITUAL EXPERIENCES</h1>
    <p class="group-subtitle">A drop-in group at</p>
  </header>
  <div class="group-copy">
    <p>Clara and Maya invite you to drop in and share any spiritual experi-<br>ences you may have had, enlightened moments, or developing<br>spiritual gifts, in a supportive environment.</p>
    <p>Perhaps you feel that you are the only one experiencing what<br>you do and would like to talk about it, or listen to others expe-<br>riences. In the group you can share with like-minded souls for<br>personal development and inspiration.</p>
    <p>Clara Wynne – has loved all things spiritual from an early age and<br>provides email consultations, spiritual counselling, and quiet<br>harbour days clara.wynne@harbourmail.co.uk 01206 555014</p>
    <p>Maya Holt – had a spiritual awakening and became open to<br>angels, is sensitive to energies, and has been on a pathway of<br>self-discovery ever since. She enjoys emotionally supporting<br>others on their life journey.</p>
    <p>Please contact Clara for future dates.</p>
  </div>
  <p class="group-venue">The Larkfield Centre, 9 Abbey Lane, Colchester<br>Contribution: £5</p>
</section>

<section class="flyer-side side-home">
  <h2 class="home-title">QUIET HARBOUR</h2>
  <p class="home-address">@ The Meditation Room, 14 Orchard Close,<br>Colchester CO1 4ZZ</p>

  <div class="price-list">
    <div class="service-name">Spiritual Counselling</div>
    <div class="service-row row-tall"><span>Up to an hours confidential one to<br>one support and assistance</span><span class="service-price">£45</span></div>
    <div class="service-name">Private email guidance</div>
    <div class="service-row row-short"><span>Response within 24 hours or sooner</span><span class="service-price">£45</span></div>
    <div class="service-name">Meditation one to one</div>
    <div class="service-row row-mid"><span>Bigger or advanced assistance to<br>develop your practice</span><span class="service-price">£45</span></div>
    <div class="service-name">Quiet Harbour day</div>
    <div class="service-row row-day"><span>A day learning to re-align with your inner being</span><span class="service-price">£90</span></div>
  </div>

  <div class="meditation-figure" role="img" aria-label="Soft grey illustration of a seated figure in a meditation pose"></div>

  <footer class="contact-band">
    <div class="contact-line" style="top:18px"><span class="contact-label">Please book on line at</span><span class="contact-sep">:</span><span class="contact-value">www.clarawynne.co.uk</span></div>
    <div class="contact-line" style="top:44px"><span class="contact-label">or email</span><span class="contact-sep">:</span><span class="contact-value">clara.wynne@harbourmail.co.uk</span></div>
    <div class="contact-line" style="top:70px"><span class="contact-label">Telephone</span><span class="contact-sep">:</span><span class="contact-value">01206 555014</span></div>
  </footer>
</section>

</body>
</html>
```